Podcast Cover Design - Headline At Quiet Tables

We renamed our podcast from the "Harborline Property Podcast" to "Headlines At Quiet Tables" and we need a new podcast cover design, Instagram profile picture, and a YouTube banner.

More so we're looking for some sort of symbol/icon. Our old logo had the Copper Lantern but we're moving to a much broader audience that isn't necessarily from Seattle and needs something that will appeal to them.

In the podcast, Dale reads the news that big media isn't covering including crime, business, homeless crisis, protests. We stay away from covering politics but our audience is mainly right-wing.

Attached are some additional designs we created in-house.

If we love the design we'll have additional job opportunities to create possible designs for merchandise.

Target Market(s)

80% Males aged 50+, Republican

Industry/Entity Type

News

Colors

Designer to choose colors to be used in the design.

Requirements
Must have
• OPEN TOO IDEAS
Nice to have
• OPEN TOO IDEAS
Should not have
• Copper Lantern

```html
<!DOCTYPE html>
<html lang="en">
<head>
<meta charset="utf-8">
<title>Headlines At Quiet Tables – Podcast Cover</title>
<link rel="stylesheet" href="https://fonts.googleapis.com/css2?family=Montserrat:wght@500;700;800&display=swap">
<style>
  :root {
    --page-bg: #ffffff;
    --cover-blue: #15729c;
    --accent-red: #dc3535;
    --ink-black: #111111;
    --text-white: #ffffff;
  }
  * { margin: 0; padding: 0; box-sizing: border-box; }
  html, body {
    width: 1200px;
    height: 1031px;
    overflow: hidden;
    background: var(--page-bg);
    font-family: "Montserrat", Arial, sans-serif;
  }
  .cover {
    position: absolute;
    left: 230px;
    top: 145px;
    width: 740px;
    height: 740px;
    background: var(--cover-blue);
    overflow: hidden;
  }
  .brand-mark {
    position: absolute;
    left: 270px;
    top: 90px;
    width: 200px;
    height: 220px;
    display: flex;
    flex-direction: column;
    align-items: center;
    justify-content: center;
    gap: 18px;
  }
  .brand-mark .dot {
    width: 120px;
    height: 120px;
    border-radius: 50%;
    background: var(--accent-red);
    border: 7px solid var(--ink-black);
  }
  .brand-mark .label {
    color: var(--text-white);
    font-weight: 700;
    font-size: 24px;
    letter-spacing: 0.5px;
  }
  .title {
    position: absolute;
    left: 0;
    right: 0;
    top: 345px;
    text-align: center;
    color: var(--text-white);
    font-weight: 800;
    line-height: 1;
  }
  .title .kicker {
    display: block;
    font-size: 49px;
    letter-spacing: 1px;
    margin-bottom: 14px;
  }
  .title .main {
    display: block;
    font-size: 92px;
    letter-spacing: -1px;
    line-height: 0.95;
  }
  .host-band {
    position: absolute;
    left: 0;
    right: 0;
    top: 670px;
    height: 70px;
    background: var(--accent-red);
  }
  .host-badge {
    position: absolute;
    left: 129px;
    top: 658px;
    width: 78px;
    height: 78px;
    border-radius: 50%;
    background: var(--text-white);
  }
  .host-badge svg { width: 78px; height: 78px; display: block; }
  .host-line {
    position: absolute;
    left: 228px;
    top: 687px;
    color: var(--text-white);
    font-weight: 500;
    font-size: 26px;
    letter-spacing: 0.5px;
    white-space: nowrap;
  }
</style>
</head>
<body>
  <main class="cover">
    <div class="brand-mark">
      <span class="dot" aria-hidden="true"></span>
      <span class="label">PODCAST</span>
    </div>

    <h1 class="title">
      <span class="kicker">HEADLINES AT</span>
      <span class="main">QUIET</span>
      <span class="main">TABLES</span>
    </h1>

    <div class="host-band"></div>
    <div class="host-badge">
      <svg viewBox="0 0 78 78" aria-hidden="true">
        <rect x="32" y="16" width="14" height="30" rx="7" fill="var(--accent-red)"/>
        <path d="M26 38 v3 a13 13 0 0 0 26 0 v-3" fill="none" stroke="var(--accent-red)" stroke-width="3" stroke-linecap="round"/>
        <line x1="39" y1="54" x2="39" y2="64" stroke="var(--accent-red)" stroke-width="3"/>
        <line x1="31" y1="64" x2="47" y2="64" stroke="var(--accent-red)" stroke-width="3" stroke-linecap="round"/>
      </svg>
    </div>
    <p class="host-line">WITH HOST DALE WHITCOMBE</p>
  </main>
</body>
</html>
```